Willow Ridge Coffee Company Label

I am in need of a label for my coffee brand. I've attached my logo, and the label I've composed in the past. This brand has not launched yet, but we will launch within the week. I'm trying to identify other label options. I am familiar with Adobe Illustrator, enough to design what I have. What I'd like is a logo that is scalable, meaning I can easily change the name of the coffee. For consistency I'd like all of my roasts to have the same label, just different names and descriptions. I've included specs for the label, I'll be using the 3x4 labels for 16 oz bags. When you submit your design please follow the specs. There needs to be my company name and address on the label, however I don't want it to take over the label.

Please reply with any questions or clarifications.

Thank you,

Ned

```html
<!DOCTYPE html>
<html lang="en">
<head>
<meta charset="utf-8">
<title>Willow Ridge Coffee Company – Open Road Roast Labels</title>
<link rel="stylesheet" href="https://fonts.googleapis.com/css2?family=Bebas+Neue&family=Kaushan+Script&family=Cormorant+Garamond:wght@400;500&family=Montserrat:wght@400&family=Oswald:wght@600&display=swap">
<style>
  :root {
    --page: #ffffff;
    --ink-white: #ffffff;
    --shadow-plum: #3a1230;
    --copy-pink: #f3d6e0;
    --copy-peach: #fbe0cf;
    --dusk-top: #f2878f;
    --dusk-haze: #f4b4aa;
    --dusk-ridge: #b07ca8;
    --dusk-forest: #7c4c78;
    --dusk-field: #561c44;
    --dusk-base: #2a1428;
    --dawn-top: #fff2c6;
    --dawn-haze: #f8c877;
    --dawn-ridge: #e7862f;
    --dawn-forest: #c95a2c;
    --dawn-field: #8e3330;
    --dawn-base: #3c0e35;
  }
  * { margin: 0; padding: 0; box-sizing: border-box; }
  html, body {
    width: 847px; height: 1200px; overflow: hidden;
    background: var(--page);
  }
  .sheet {
    position: relative; width: 847px; height: 1200px;
  }
  .label {
    position: absolute; top: 676px;
    width: 314px; height: 418px;
    overflow: hidden;
    color: var(--ink-white);
  }
  .label--dusk { left: 73px; }
  .label--dawn { left: 460px; }
  .label__scene {
    position: absolute; inset: 0;
  }
  .label--dusk .label__scene {
    background: linear-gradient(180deg,
      var(--dusk-top) 0%, var(--dusk-haze) 20%, var(--dusk-ridge) 33%,
      var(--dusk-forest) 42%, var(--dusk-field) 62%, var(--dusk-base) 100%);
  }
  .label--dawn .label__scene {
    background: linear-gradient(180deg,
      var(--dawn-top) 0%, var(--dawn-haze) 20%, var(--dawn-ridge) 33%,
      var(--dawn-forest) 42%, var(--dawn-field) 62%, var(--dawn-base) 100%);
  }
  .label__title {
    position: absolute; left: 0; right: 0; top: 42px;
    text-align: center;
    font-family: "Bebas Neue", "Oswald", sans-serif;
    font-weight: 400;
    font-size: 78px; line-height: 1;
    letter-spacing: -1px;
    white-space: nowrap;
    text-shadow: 3px 3px 0 var(--shadow-plum);
  }
  .label__subtitle {
    position: absolute; left: 124px; top: 110px;
    font-family: "Kaushan Script", cursive;
    font-size: 30px; line-height: 1;
    text-shadow: 2px 2px 0 var(--shadow-plum);
  }
  .label__description {
    position: absolute; left: 108px; top: 179px;
    width: 142px;
    font-family: "Cormorant Garamond", serif;
    font-size: 11px; line-height: 13.5px;
  }
  .label--dusk .label__description { color: var(--copy-pink); }
  .label--dawn .label__description { color: var(--copy-peach); }
  .brand {
    position: absolute; left: 19px; top: 322px;
    display: flex; align-items: center; gap: 6px;
  }
  .brand__dot {
    width: 16px; height: 16px; border-radius: 50%;
    background: var(--ink-white);
  }
  .brand__name {
    font-family: "Cormorant Garamond", serif;
    font-weight: 500; font-size: 12px;
    white-space: nowrap;
    color: var(--ink-white);
  }
  .label__maker {
    position: absolute; left: 24px; top: 354px;
    font-family: "Montserrat", sans-serif;
    font-size: 9.5px; line-height: 13px;
    letter-spacing: 0.3px;
  }
  .label__weight {
    position: absolute; left: 24px; top: 386px;
    font-family: "Oswald", sans-serif;
    font-weight: 600; font-size: 12px;
    letter-spacing: 0.2px;
    white-space: nowrap;
  }
</style>
</head>
<body>
<main class="sheet">
  <section class="label label--dusk">
    <div class="label__scene" role="img" aria-label="Pink dusk illustration: snowy mountain peak, pine forest and a winding road through purple fields"></div>
    <h1 class="label__title">OPEN ROAD</h1>
    <p class="label__subtitle">Roast</p>
    <p class="label__description">Smooth as a morning drive, bold enough for espresso. Pairs well with every mile of your journey.</p>
    <div class="brand">
      <span class="brand__dot"></span>
      <span class="brand__name">Willow Ridge Coffee Co.</span>
    </div>
    <p class="label__maker">Manufactured for:<br>Street address</p>
    <p class="label__weight">NET WT. 16 OZ. (454g)</p>
  </section>

  <section class="label label--dawn">
    <div class="label__scene" role="img" aria-label="Golden dawn illustration: snowy mountain peak, orange pine forest and a winding road through red fields"></div>
    <h1 class="label__title">OPEN ROAD</h1>
    <p class="label__subtitle">Roast</p>
    <p class="label__description">Smooth as a morning drive, bold enough for espresso. Pairs well with every mile of your journey.</p>
    <div class="brand">
      <span class="brand__dot"></span>
      <span class="brand__name">Willow Ridge Coffee Co.</span>
    </div>
    <p class="label__maker">Manufactured for:<br>Street address</p>
    <p class="label__weight">NET WT. 16 OZ. (454g)</p>
  </section>
</main>
</body>
</html>
```